Wine Label for a Sweet Wine Called "Glimmo"

We need a wine label that will be used for both a sweet red and a sweet white wine. The very important thing to remember is the target market for these wines is: young American women who love sweet wines and they also spend a lot of their money on their hair, clothes, jewelry, nails. They LOVE Glimmo (Glimmo is a word used to describe flashy accessories, jewelry, decoration.) This label needs to be eye catching, showy, fun, glittery. Please put the brand name, "Glimmo," big, and then in smaller but still readable words underneath the label or somewhere on the label: Sweet, Sophisticated, Red (or white). (An example of what I mean is attached). To differentiate between the two color wines you can suggest color changes to differentiate between the red label and the white label but the label design itself should be the same. Ultimately, the label can be the exact same label for both white and red as long as it looks good on a white wine (a greenish/yellow wine in a clear glass bottle) and a red wine (a dark color wine in a dark bottle).

I've attached an example of the text size relationship between the word Glimmo and the words to go underneath or elsewhere on the label, but you can certainly play with this-- it is just a suggestion of the text size relationship, and definitely NOT at all mandatory that you use any of these fonts.

You can pick the size of the label but try to stay within normal wine label sizes, meaning don't go bigger than approx. 3.5 inches wide and 5 inches tall.

Target Market(s)

Young American women who love sweet wines and spend a lot of money on their hair, clothes, jewelry, nails. They love Glimmo (Glimmo is a word that means flashy accessories, jewelry, decoration)

Requirements
Must have
• It needs to be flashy, glittery, fun, eye catching, memorable
Nice to have
• It shouldn't be too too ultra feminine! The target market is strong independent women and we also have men who will buy it too.

```html
<!DOCTYPE html>
<html lang="en">
<head>
<meta charset="utf-8">
<title>Glimmo Wine Label</title>
<link rel="stylesheet" href="https://fonts.googleapis.com/css2?family=Oswald:wght@200;400&display=swap">
<style>
  :root {
    --page-bg: #ebebeb;
    --label-bg: #070707;
    --gold: #f2c21b;
    --gold-deep: #d9a514;
    --glow-core: #fff6c2;
    --glow-mid: #f5cf3a;
    --ink-light: #ffffff;
  }
  * { margin: 0; padding: 0; box-sizing: border-box; }
  html, body {
    width: 1079px;
    height: 1200px;
    overflow: hidden;
    background: var(--page-bg);
  }
  .wine-label {
    position: absolute;
    left: 144px;
    top: 159px;
    width: 795px;
    height: 890px;
    background: var(--label-bg);
    overflow: hidden;
  }
  .dotted-frame,
  .glitter-glow {
    position: absolute;
    left: 0;
    top: 0;
    width: 795px;
    height: 890px;
  }
  .brand-name {
    position: absolute;
    left: 0;
    width: 795px;
    top: 279px;
    text-align: center;
    font-family: "Oswald", sans-serif;
    font-weight: 400;
    font-size: 218px;
    line-height: 1;
    letter-spacing: 0;
    color: var(--gold);
  }
  .tagline {
    position: absolute;
    left: 0;
    width: 795px;
    top: 590px;
    text-align: center;
    font-family: "Oswald", sans-serif;
    font-weight: 200;
    font-size: 36px;
    line-height: 1;
    letter-spacing: 4.5px;
    word-spacing: 6px;
    color: var(--ink-light);
  }
</style>
</head>
<body>
  <main class="wine-label">
    <svg class="dotted-frame" viewBox="0 0 795 890" aria-hidden="true">
      <g fill="none" stroke-linecap="round">
        <rect x="35" y="33" width="729" height="819" stroke="var(--gold)" stroke-width="6" stroke-dasharray="0 10"/>
        <rect x="42" y="40" width="715" height="805" stroke="var(--gold-deep)" stroke-width="5" stroke-dasharray="0 10" stroke-dashoffset="5"/>
        <rect x="49" y="47" width="701" height="791" stroke="var(--gold)" stroke-width="5" stroke-dasharray="0 10"/>
      </g>
    </svg>
    <svg class="glitter-glow" viewBox="0 0 795 890" role="img" aria-label="Gold glitter sparkle glow around the brand name">
      <defs>
        <radialGradient id="sparkle-glow">
          <stop offset="0" stop-color="var(--glow-core)" stop-opacity="0.9"/>
          <stop offset="0.35" stop-color="var(--glow-mid)" stop-opacity="0.35"/>
          <stop offset="1" stop-color="var(--glow-mid)" stop-opacity="0"/>
        </radialGradient>
        <radialGradient id="name-haze">
          <stop offset="0" stop-color="var(--glow-mid)" stop-opacity="0.16"/>
          <stop offset="1" stop-color="var(--glow-mid)" stop-opacity="0"/>
        </radialGradient>
      </defs>
      <ellipse cx="397" cy="400" rx="340" ry="170" fill="url(#name-haze)"/>
      <circle cx="156" cy="290" r="60" fill="url(#sparkle-glow)"/>
      <circle cx="532" cy="362" r="48" fill="url(#sparkle-glow)"/>
    </svg>
    <h1 class="brand-name">Glimmo</h1>
    <p class="tagline">SWEET | RED | SOPHISTICATED</p>
  </main>
</body>
</html>
```